Plumbing Products Website

This project is to create a web page for Mr. Clear Brook and Mr. Hot Kettle's product offerings. There are 14 unique products. The main page will showcase all 14 products arranged in a clean, concise format that flows nicely and is easy to read.
Furthermore, I need a unique page for each of the 14 products that the main page can link the products to so visitors can click each of them to "Learn More".
For reference, our websites are MrBrookly.example and TopBoilerHub.example; so keep the branding, color-scheme, header, footer, etc. consistent with MrBrookly.example and TopBoilerHub.example.
For reference, here is the catalog. Feel free to copy as much of the content as necessary to build the pages:
https://catalogs.pagefolio.example/MrHotKettle/qvtx/
For clarification, the products are:
1. Whole House Water Purification System
2. Whole House Water Ionization System
3. Whole House Water Softener System
4. Water Heater Sediment Pre-Filter
5. Whole-House UV Water Sterilization System
6. The ULTIMATE Whole House Water Treatment System
7. Under-Sink Reverse Osmosis System with UV Sterilizer
8. Smart Water Heater Regulator with Automated Stand-By for Power Savings
9. Whole House Water Pressure Booster
10. Hot Water Heater Tank Volume Booster
11. Leak Detector with Automatic Water Shutoff
12. Whole House UV Air Purification System
13. Leak Detector Alarm with Mobile App
14. Multi-Gas Detector for Carbon Monoxide, Natural Gas, Propane, Methane, Explosive Gasses, Smoke & Fire
Unfortunately, all the content was created by AI, so I don't have any "original" images or other media. I have attached the logos for your reference though. Also, each individual catalog page is attached.
Once the winning design is chosen, I will need the pages coded and hosted on a staging server for me to view in a live environment before I move them to my server.
Let me know if you have any questions.

```html
<!DOCTYPE html>
<html lang="en">
<head>
<meta charset="utf-8">
<title>Mr. Clear Brook &amp; Mr. Hot Kettle — Page Designs</title>
<link href="https://fonts.googleapis.com/css2?family=Poppins:wght@400;500;600;700;800&display=swap" rel="stylesheet">
<style>
:root{
  --navy:#0a1d47;
  --blue:#1f4fb4;
  --blue-dark:#173c93;
  --blue-text:#1a3f9e;
  --sky:#dbe8fb;
  --sky-2:#a9c8f2;
  --ink:#2b3140;
  --muted:#5d6575;
  --line:#dfe5ef;
  --white:#ffffff;
  --star:#f4b41a;
}
*{margin:0;padding:0;box-sizing:border-box}
html,body{width:800px;height:1200px;overflow:hidden;background:var(--navy);font-family:"Poppins",sans-serif;color:var(--ink)}
.board{position:relative;width:800px;height:1200px;overflow:hidden}
.tab{position:absolute;top:0;height:26px;background:var(--blue);color:var(--white);font-weight:700;font-size:12px;display:flex;align-items:center;justify-content:center;border-radius:0 0 4px 4px;letter-spacing:.2px}
.page{position:absolute;background:var(--white);border-radius:6px 6px 0 0;overflow:hidden}
.abs{position:absolute}
/* header */
.site-header{position:absolute;left:0;top:0;right:0;height:47px;display:flex;align-items:center;padding:0 12px;background:var(--white)}
.brand{display:flex;align-items:center;gap:5px}
.brand-dot{width:20px;height:20px;border-radius:50%;background:var(--blue)}
.brand-name{color:var(--blue-text);font-weight:700;font-size:7px;line-height:1.25}
.nav{display:flex;gap:9px;margin-left:auto;font-size:4.2px;font-weight:600;color:var(--ink)}
.nav .on{color:var(--blue)}
.call{display:flex;align-items:center;gap:3px;margin-left:12px;font-size:4px;color:var(--blue-text);line-height:1.3}
.call b{font-size:4.6px}
/* buttons */
.btn{display:inline-flex;align-items:center;justify-content:center;font-weight:700;font-size:4.6px;border-radius:2px;letter-spacing:.2px}
.btn-fill{background:var(--blue-dark);color:var(--white)}
.btn-line{border:1px solid var(--blue);color:var(--blue);background:var(--white)}
.btn-white{background:var(--white);color:var(--blue-dark)}
.ph{position:absolute;border-radius:3px}
.sec-title{position:absolute;left:0;right:0;text-align:center;color:var(--blue-text);font-weight:700}
.sec-sub{position:absolute;left:0;right:0;text-align:center;color:var(--muted);font-size:5px}
/* product cards */
.grid{position:absolute;display:flex}
.pcard{position:relative;border:1px solid var(--line);border-radius:4px;background:var(--white);text-align:center;box-shadow:0 1px 2px rgba(20,40,90,.06)}
.pcard .num{position:absolute;left:4px;top:4px;width:10px;height:10px;border-radius:50%;background:var(--blue-dark);color:var(--white);font-size:5px;font-weight:700;display:flex;align-items:center;justify-content:center}
.pcard .img{margin:16px auto 0;width:44px;height:40px;border-radius:3px;background:linear-gradient(160deg,#e9eef6,#9fb0c8 55%,#2d3a52)}
.pcard .name{margin-top:7px;font-size:4.6px;font-weight:600;color:var(--blue-text);line-height:1.45;padding:0 3px}
.pcard .more{margin-top:3px;font-size:4px;font-weight:600;color:var(--blue)}
/* icon rows */
.ic{display:flex;align-items:center;justify-content:center;border-radius:50%}
.check{width:6px;height:6px;border-radius:50%;background:var(--blue-dark);display:inline-flex;align-items:center;justify-content:center;flex:none}
</style>
</head>
<body>
<div class="board">

<!-- tabs -->
<div class="tab" style="left:150px;width:100px">HOME PAGE</div>
<div class="tab" style="left:527px;width:155px">PRODUCT DETAILS PAGE</div>
<div class="tab" style="left:543px;top:783px;width:114px;height:24px;border-radius:4px 4px 0 0">ABOUT US PAGE</div>

<!-- ================= HOME PAGE ================= -->
<section class="page home" style="left:10px;top:27px;width:390px;height:1173px">
  <header class="site-header">
    <div class="brand"><span class="brand-dot"></span><div class="brand-name">Mr. Clear Brook<br>Mr. Hot Kettle</div></div>
    <nav class="nav"><span class="on">HOME</span><span>PRODUCTS ⌄</span><span>ABOUT US</span><span>WHY CHOOSE US</span><span>RESOURCES ⌄</span><span>CONTACT US</span></nav>
    <div class="call"><svg width="8" height="8" viewBox="0 0 24 24"><path d="M6.6 10.8a15 15 0 006.6 6.6l2.2-2.2c.3-.3.7-.4 1-.2 1.1.4 2.3.6 3.6.6.6 0 1 .4 1 1V20c0 .6-.4 1-1 1A17 17 0 013 4c0-.6.4-1 1-1h3.5c.6 0 1 .4 1 1 0 1.3.2 2.5.6 3.6.1.3 0 .7-.2 1z" fill="#1f4fb4"/></svg><div>Call Us Now<br><b>(555) 014-2290</b></div></div>
  </header>

  <!-- hero -->
  <div class="ph" style="left:0;top:47px;width:390px;height:188px;border-radius:0;background:linear-gradient(90deg,#f4f7fc 40%,#e7edf6)"></div>
  <div class="ph" role="img" aria-label="Family filling glasses with filtered water at a kitchen sink" style="left:175px;top:47px;width:215px;height:170px;border-radius:0;background:linear-gradient(135deg,#e8e2da,#c9b7a3 45%,#8ea6c4)"></div>
  <div class="ph" role="img" aria-label="Splashing water wave" style="left:0;top:200px;width:390px;height:36px;border-radius:0;background:linear-gradient(180deg,rgba(255,255,255,0),#b9d4f4 55%,#4f86d8)"></div>
  <h1 class="abs" style="left:22px;top:71px;font-size:22px;font-weight:800;color:var(--blue-text);line-height:1.15;letter-spacing:-.3px">PURE WATER.<br>BETTER LIVING.</h1>
  <p class="abs" style="left:22px;top:130px;width:140px;font-size:6.4px;line-height:1.55;color:var(--ink)">Complete solutions for clean, safe and great-tasting water throughout your entire home.</p>
  <span class="btn btn-fill abs" style="left:22px;top:176px;width:66px;height:16px">EXPLORE PRODUCTS</span>
  <span class="btn btn-line abs" style="left:93px;top:176px;width:78px;height:16px">GET A FREE CONSULTATION</span>

  <!-- feature band -->
  <div class="abs" style="left:0;top:236px;width:390px;height:42px;background:var(--blue);display:flex;justify-content:space-around;align-items:center;padding:0 14px">
    <div style="display:flex;align-items:center;gap:4px;color:#fff;font-size:4.6px;font-weight:600;line-height:1.4"><span class="ic" style="width:18px;height:18px;border:1px solid #fff"><svg width="9" height="9" viewBox="0 0 24 24"><path d="M3 11l9-7 9 7v9H3z" fill="none" stroke="#fff" stroke-width="2"/></svg></span>WHOLE HOME<br>SOLUTIONS</div>
    <div style="display:flex;align-items:center;gap:4px;color:#fff;font-size:4.6px;font-weight:600;line-height:1.4"><span class="ic" style="width:18px;height:18px;border:1px solid #fff"><svg width="9" height="9" viewBox="0 0 24 24"><path d="M12 2l8 3v6c0 5-3.5 9-8 11-4.5-2-8-6-8-11V5z" fill="none" stroke="#fff" stroke-width="2"/></svg></span>PROTECT YOUR<br>FAMILY &amp; HOME</div>
    <div style="display:flex;align-items:center;gap:4px;color:#fff;font-size:4.6px;font-weight:600;line-height:1.4"><span class="ic" style="width:18px;height:18px;border:1px solid #fff"><svg width="9" height="9" viewBox="0 0 24 24"><path d="M12 3c4 5 6 8 6 11a6 6 0 01-12 0c0-3 2-6 6-11z" fill="none" stroke="#fff" stroke-width="2"/></svg></span>SAVE ENERGY<br>&amp; MONEY</div>
    <div style="display:flex;align-items:center;gap:4px;color:#fff;font-size:4.6px;font-weight:600;line-height:1.4"><span class="ic" style="width:18px;height:18px;border:1px solid #fff"><svg width="9" height="9" viewBox="0 0 24 24"><circle cx="12" cy="12" r="4" fill="none" stroke="#fff" stroke-width="2"/><path d="M12 2v4M12 18v4M2 12h4M18 12h4" stroke="#fff" stroke-width="2"/></svg></span>PROFESSIONAL<br>INSTALLATION</div>
    <div style="display:flex;align-items:center;gap:4px;color:#fff;font-size:4.6px;font-weight:600;line-height:1.4"><span class="ic" style="width:18px;height:18px;border:1px solid #fff"><svg width="9" height="9" viewBox="0 0 24 24"><path d="M5 12l5 5 9-10" fill="none" stroke="#fff" stroke-width="2"/></svg></span>LIFETIME<br>SUPPORT</div>
  </div>

  <!-- products -->
  <h2 class="sec-title" style="top:292px;font-size:10px">OUR PRODUCT SOLUTIONS</h2>
  <p class="sec-sub" style="top:309px">Advanced water and air treatment systems for your entire home.</p>

  <div class="grid" style="left:14px;top:331px;gap:6px">
    <div class="pcard" style="width:69px;height:116px"><span class="num">1</span><div class="img" role="img" aria-label="Purification system"></div><div class="name">Whole House<br>Water Purification<br>System</div><div class="more">Learn More →</div></div>
    <div class="pcard" style="width:69px;height:116px"><span class="num">2</span><div class="img" role="img" aria-label="Ionization system"></div><div class="name">Whole House<br>Water Ionization<br>System</div><div class="more">Learn More →</div></div>
    <div class="pcard" style="width:69px;height:116px"><span class="num">3</span><div class="img" role="img" aria-label="Softener system"></div><div class="name">Whole House<br>Water Softener<br>System</div><div class="more">Learn More →</div></div>
    <div class="pcard" style="width:69px;height:116px"><span class="num">4</span><div class="img" role="img" aria-label="Sediment pre-filter"></div><div class="name">Water Heater<br>Sediment Pre-Filter</div><div class="more">Learn More →</div></div>
    <div class="pcard" style="width:69px;height:116px"><span class="num">5</span><div class="img" role="img" aria-label="UV sterilization system"></div><div class="name">Whole-House UV<br>Water Sterilization<br>System</div><div class="more">Learn More →</div></div>
  </div>
  <div class="grid" style="left:14px;top:455px;gap:6px">
    <div class="pcard" style="width:69px;height:116px"><span class="num">6</span><div class="img" role="img" aria-label="Ultimate treatment system"></div><div class="name">The ULTIMATE<br>Whole House Water<br>Treatment System</div><div class="more">Learn More →</div></div>
    <div class="pcard" style="width:69px;height:116px"><span class="num">7</span><div class="img" role="img" aria-label="Reverse osmosis system"></div><div class="name">Under-Sink Reverse<br>Osmosis System with<br>UV Sterilizer</div><div class="more">Learn More →</div></div>
    <div class="pcard" style="width:69px;height:116px"><span class="num">8</span><div class="img" role="img" aria-label="Smart water heater regulator"></div><div class="name">Smart Water Heater<br>Regulator with Automated<br>Stand-By for Power Savings</div><div class="more">Learn More →</div></div>
    <div class="pcard" style="width:69px;height:116px"><span class="num">9</span><div class="img" role="img" aria-label="Pressure booster pump"></div><div class="name">Whole House<br>Water Pressure<br>Booster</div><div class="more">Learn More →</div></div>
    <div class="pcard" style="width:69px;height:116px"><span class="num">10</span><div class="img" role="img" aria-label="Tank volume booster"></div><div class="name">Hot Water Heater<br>Tank Volume<br>Booster</div><div class="more">Learn More →</div></div>
  </div>
  <div class="grid" style="left:37px;top:581px;gap:8px">
    <div class="pcard" style="width:74px;height:110px"><span class="num">11</span><div class="img" role="img" aria-label="Leak detector with shutoff valve"></div><div class="name">Leak Detector with<br>Automatic Water<br>Shutoff</div><div class="more">Learn More →</div></div>
    <div class="pcard" style="width:74px;height:110px"><span class="num">12</span><div class="img" role="img" aria-label="UV air purification unit"></div><div class="name">Whole House<br>UV Air Purification<br>System</div><div class="more">Learn More →</div></div>
    <div class="pcard" style="width:74px;height:110px"><span class="num">13</span><div class="img" role="img" aria-label="Leak detector alarm"></div><div class="name">Leak Detector Alarm<br>with Mobile App</div><div class="more">Learn More →</div></div>
    <div class="pcard" style="width:74px;height:110px"><span class="num">14</span><div class="img" role="img" aria-label="Multi-gas detector"></div><div class="name">Multi-Gas Detector<br>for Carbon Monoxide,<br>Natural Gas &amp; More</div><div class="more">Learn More →</div></div>
  </div>

  <!-- why choose -->
  <div class="abs" style="left:0;top:700px;width:390px;height:127px;background:var(--blue);border-radius:8px 8px 0 0;color:#fff;text-align:center">
    <h2 style="margin-top:12px;font-size:9.6px;font-weight:700">WHY CHOOSE MR. CLEAR BROOK &amp; MR. HOT KETTLE?</h2>
    <p style="font-size:5px;margin-top:3px;opacity:.9">Trusted by homeowners across Florida for over a decade.</p>
    <div style="display:flex;justify-content:space-around;padding:10px 20px 0;font-size:4.5px;line-height:1.5">
      <div><span class="ic" style="width:16px;height:16px;margin:0 auto 4px"><svg width="12" height="12" viewBox="0 0 24 24"><path d="M12 3c4 5 6 8 6 11a6 6 0 01-12 0c0-3 2-6 6-11z" fill="none" stroke="#fff" stroke-width="1.6"/></svg></span><b style="font-size:5px">Expert Solutions</b><br>Industry-leading<br>technology and<br>innovation</div>
      <div><span class="ic" style="width:16px;height:16px;margin:0 auto 4px"><svg width="12" height="12" viewBox="0 0 24 24"><circle cx="12" cy="12" r="8" fill="none" stroke="#fff" stroke-width="1.6"/><path d="M8 12l3 3 5-6" fill="none" stroke="#fff" stroke-width="1.6"/></svg></span><b style="font-size:5px">Premium Quality</b><br>Top-grade components<br>for long-lasting<br>performance</div>
      <div><span class="ic" style="width:16px;height:16px;margin:0 auto 4px"><svg width="12" height="12" viewBox="0 0 24 24"><rect x="4" y="4" width="16" height="16" rx="3" fill="none" stroke="#fff" stroke-width="1.6"/><path d="M8 12h8M12 8v8" stroke="#fff" stroke-width="1.6"/></svg></span><b style="font-size:5px">Professional Service</b><br>Certified installation<br>and dedicated<br>support</div>
      <div><span class="ic" style="width:16px;height:16px;margin:0 auto 4px"><svg width="12" height="12" viewBox="0 0 24 24"><path d="M12 2l8 3v6c0 5-3.5 9-8 11-4.5-2-8-6-8-11V5z" fill="none" stroke="#fff" stroke-width="1.6"/></svg></span><b style="font-size:5px">Local &amp; Trusted</b><br>Proudly serving<br>Florida homes and<br>businesses</div>
      <div><span class="ic" style="width:16px;height:16px;margin:0 auto 4px"><svg width="12" height="12" viewBox="0 0 24 24"><path d="M5 19c0-8 6-13 14-14-1 8-6 14-14 14zM5 19l7-7" fill="none" stroke="#fff" stroke-width="1.6"/></svg></span><b style="font-size:5px">Eco-Friendly</b><br>Sustainable solutions<br>for a cleaner<br>environment</div>
    </div>
  </div>

  <!-- CTA -->
  <div class="abs" role="img" aria-label="Water splash and glass of water" style="left:0;top:827px;width:390px;height:102px;background:linear-gradient(180deg,#cfe1f8,#eef4fc 40%,#9cc0ee)"></div>
  <h2 class="abs" style="left:0;width:390px;top:846px;text-align:center;font-size:11px;font-weight:700;color:var(--blue-text)">Ready for Better Water?</h2>
  <p class="abs" style="left:0;width:390px;top:864px;text-align:center;font-size:5px;color:var(--ink)">Get a free water analysis and expert recommendation for your home.</p>
  <span class="btn btn-fill abs" style="left:141px;top:885px;width:102px;height:17px">SCHEDULE FREE CONSULTATION</span>

  <!-- stats -->
  <div class="abs" style="left:0;top:929px;width:390px;height:51px;background:var(--blue-dark);display:flex;align-items:center;color:#fff;text-align:center">
    <div style="flex:1;border-right:1px solid rgba(255,255,255,.3)"><div style="font-size:13px;font-weight:600">15+</div><div style="font-size:5px;line-height:1.4">Years of Trusted<br>Service</div></div>
    <div style="flex:1;border-right:1px solid rgba(255,255,255,.3)"><div style="font-size:13px;font-weight:600">10K+</div><div style="font-size:5px;line-height:1.4">Happy<br>Customers</div></div>
    <div style="flex:1;border-right:1px solid rgba(255,255,255,.3)"><div style="font-size:13px;font-weight:600">100%</div><div style="font-size:5px;line-height:1.4">Satisfaction<br>Guaranteed</div></div>
    <div style="flex:1"><div style="font-size:12px;font-weight:600">Top Rated</div><div style="font-size:5px;line-height:1.4">in Florida</div></div>
  </div>

  <!-- testimonials -->
  <h2 class="sec-title" style="top:990px;font-size:9px">WHAT OUR CUSTOMERS SAY</h2>
  <div class="grid" style="left:20px;top:1010px;gap:10px">
    <div class="pcard" style="width:110px;height:70px;text-align:left;padding:7px 8px">
      <div style="color:var(--blue);font-weight:800;font-size:10px;line-height:1">❝</div>
      <p style="font-size:4.6px;line-height:1.55;margin-top:5px">The water quality in our home has never been better. Highly recommend their whole house system!</p>
      <div style="display:flex;justify-content:space-between;margin-top:6px;font-size:4.6px;font-weight:600;color:var(--blue-text)"><span>– Dana R.</span><span style="color:var(--star)">★★★★★</span></div>
    </div>
    <div class="pcard" style="width:110px;height:70px;text-align:left;padding:7px 8px">
      <div style="color:var(--blue);font-weight:800;font-size:10px;line-height:1">❝</div>
      <p style="font-size:4.6px;line-height:1.55;margin-top:5px">Professional installation and excellent customer service. Our water is soft, clean and great tasting!</p>
      <div style="display:flex;justify-content:space-between;margin-top:6px;font-size:4.6px;font-weight:600;color:var(--blue-text)"><span>– Owen P.</span><span style="color:var(--star)">★★★★★</span></div>
    </div>
    <div class="pcard" style="width:110px;height:70px;text-align:left;padding:7px 8px">
      <div style="color:var(--blue);font-weight:800;font-size:10px;line-height:1">❝</div>
      <p style="font-size:4.6px;line-height:1.55;margin-top:5px">We noticed the difference immediately. Great products and knowledgeable team!</p>
      <div style="display:flex;justify-content:space-between;margin-top:10px;font-size:4.6px;font-weight:600;color:var(--blue-text)"><span>– Mia L.</span><span style="color:var(--star)">★★★★★</span></div>
    </div>
  </div>
  <div class="abs" role="img" aria-label="Rolling water wave" style="left:0;top:1098px;width:390px;height:75px;background:linear-gradient(180deg,#ffffff,#bcd5f3 40%,#4e86d6 80%,#1f4fb4)"></div>
</section>

<!-- ================= PRODUCT DETAILS PAGE ================= -->
<section class="page product" style="left:409px;top:27px;width:383px;height:753px">
  <header class="site-header" style="height:44px">
    <div class="brand"><span class="brand-dot"></span><div class="brand-name">Mr. Clear Brook<br>Mr. Hot Kettle</div></div>
    <nav class="nav" style="gap:8px"><span class="on">HOME</span><span>PRODUCTS ⌄</span><span>ABOUT US</span><span>WHY CHOOSE US</span><span>RESOURCES ⌄</span><span>CONTACT US</span></nav>
    <div class="call" style="margin-left:8px"><svg width="8" height="8" viewBox="0 0 24 24"><path d="M6.6 10.8a15 15 0 006.6 6.6l2.2-2.2c.3-.3.7-.4 1-.2 1.1.4 2.3.6 3.6.6.6 0 1 .4 1 1V20c0 .6-.4 1-1 1A17 17 0 013 4c0-.6.4-1 1-1h3.5c.6 0 1 .4 1 1 0 1.3.2 2.5.6 3.6.1.3 0 .7-.2 1z" fill="#1f4fb4"/></svg><div>Call Us Now<br><b>(555) 014-2290</b></div></div>
  </header>
  <p class="abs" style="left:18px;top:54px;font-size:4.6px;color:var(--muted)">Home &nbsp;›&nbsp; Products &nbsp;›&nbsp; <span style="color:var(--blue);font-weight:600">Whole House Water Purification System</span></p>

  <div class="ph" role="img" aria-label="Twin blue filter housings and stainless tank with water splash" style="left:14px;top:74px;width:170px;height:190px;background:radial-gradient(ellipse at 45% 50%,#1b52c4 0 22%,#9fbbe6 40%,#eef3fb 70%,#fff)"></div>
  <div class="abs" style="left:19px;top:270px;display:flex;gap:7px">
    <div style="width:30px;height:27px;border:1px solid var(--blue);border-radius:3px;background:linear-gradient(#eef2f8,#8aa6d6)" role="img" aria-label="Thumbnail"></div>
    <div style="width:30px;height:27px;border:1px solid var(--line);border-radius:3px;background:linear-gradient(#eef2f8,#8aa6d6)" role="img" aria-label="Thumbnail"></div>
    <div style="width:30px;height:27px;border:1px solid var(--line);border-radius:3px;background:linear-gradient(#f4f6fa,#c4ccd8)" role="img" aria-label="Thumbnail"></div>
    <div style="width:30px;height:27px;border:1px solid var(--line);border-radius:3px;background:linear-gradient(#f4f6fa,#c4ccd8)" role="img" aria-label="Thumbnail"></div>
  </div>

  <h1 class="abs" style="left:198px;top:73px;font-size:12.5px;font-weight:700;color:var(--blue-text);line-height:1.2">Whole House Water<br>Purification System</h1>
  <p class="abs" style="left:198px;top:109px;font-size:6.3px;font-weight:600;line-height:1.4">Clean, Safe &amp; Great-Tasting Water<br>Throughout Your Entire Home</p>
  <p class="abs" style="left:198px;top:136px;width:170px;font-size:4.8px;line-height:1.6;color:var(--ink)">Our advanced whole house water purification system effectively reduces harmful contaminants, chlorine, sediment, and chemicals while improving taste and odor. Enjoy purified water from every tap in your home.</p>
  <ul class="abs" style="left:198px;top:189px;list-style:none;font-size:4.8px;line-height:1;display:flex;flex-direction:column;gap:8px">
    <li style="display:flex;gap:5px;align-items:center"><span class="check"><svg width="4" height="4" viewBox="0 0 10 10"><path d="M2 5l2 2 4-4" fill="none" stroke="#fff" stroke-width="1.6"/></svg></span>Reduces chlorine, sediment, rust &amp; more</li>
    <li style="display:flex;gap:5px;align-items:center"><span class="check"><svg width="4" height="4" viewBox="0 0 10 10"><path d="M2 5l2 2 4-4" fill="none" stroke="#fff" stroke-width="1.6"/></svg></span>Protects your plumbing &amp; appliances</li>
    <li style="display:flex;gap:5px;align-items:center"><span class="check"><svg width="4" height="4" viewBox="0 0 10 10"><path d="M2 5l2 2 4-4" fill="none" stroke="#fff" stroke-width="1.6"/></svg></span>Improves skin &amp; hair health</li>
    <li style="display:flex;gap:5px;align-items:center"><span class="check"><svg width="4" height="4" viewBox="0 0 10 10"><path d="M2 5l2 2 4-4" fill="none" stroke="#fff" stroke-width="1.6"/></svg></span>Easy maintenance &amp; long-lasting performance</li>
    <li style="display:flex;gap:5px;align-items:center"><span class="check"><svg width="4" height="4" viewBox="0 0 10 10"><path d="M2 5l2 2 4-4" fill="none" stroke="#fff" stroke-width="1.6"/></svg></span>Perfect for well &amp; municipal water</li>
  </ul>
  <span class="btn btn-fill abs" style="left:198px;top:266px;width:90px;height:18px">GET A FREE CONSULTATION</span>

  <!-- how it works + specs -->
  <div class="abs" style="left:18px;top:314px;width:346px;height:206px;border:1px solid var(--line);border-radius:4px"></div>
  <h2 class="abs" style="left:18px;width:346px;top:324px;text-align:center;font-size:6.6px;font-weight:700;color:var(--blue-text)">HOW IT WORKS</h2>
  <div class="abs" style="left:60px;top:339px;width:262px;display:flex;justify-content:space-between;align-items:flex-start;text-align:center;font-size:4.8px;font-weight:600;color:var(--blue-text);line-height:1.4">
    <div style="width:50px"><span class="ic" style="width:36px;height:36px;background:#eef3fc;margin:0 auto 6px"><svg width="16" height="16" viewBox="0 0 24 24"><path d="M4 8h10v4H8v6M14 10h4v3" fill="none" stroke="#1f4fb4" stroke-width="1.6"/><path d="M8 20c0-1 1-2 1-3 0 1 1 2 1 3a1 1 0 01-2 0z" fill="#1f4fb4"/></svg></span>Tap Water</div>
    <div style="font-size:14px;color:var(--blue-dark);margin-top:10px">→</div>
    <div style="width:50px"><span class="ic" style="width:36px;height:36px;background:#eef3fc;margin:0 auto 6px"><svg width="16" height="16" viewBox="0 0 24 24"><rect x="7" y="3" width="10" height="18" rx="2" fill="none" stroke="#1f4fb4" stroke-width="1.6"/><path d="M10 7v10M14 7v10" stroke="#1f4fb4" stroke-width="1.3"/></svg></span>Multi-Stage<br>Filtration</div>
    <div style="font-size:14px;color:var(--blue-dark);margin-top:10px">→</div>
    <div style="width:50px"><span class="ic" style="width:36px;height:36px;background:#eef3fc;margin:0 auto 6px"><svg width="16" height="16" viewBox="0 0 24 24"><path d="M12 3c4 5 6 8 6 11a6 6 0 01-12 0c0-3 2-6 6-11z" fill="none" stroke="#1f4fb4" stroke-width="1.6"/><path d="M9 14l2 2 4-4" fill="none" stroke="#1f4fb4" stroke-width="1.4"/></svg></span>Purified Water<br>To Home</div>
  </div>
  <div class="abs" style="left:18px;top:410px;width:346px;height:1px;background:var(--line)"></div>
  <div class="abs" style="left:212px;top:418px;width:1px;height:96px;background:var(--line)"></div>
  <h3 class="abs" style="left:32px;top:420px;font-size:5.8px;font-weight:700;color:var(--blue-text)">TECHNICAL SPECIFICATIONS</h3>
  <table class="abs" style="left:32px;top:433px;width:170px;font-size:4.4px;border-collapse:collapse;line-height:1">
    <tbody>
      <tr style="border-bottom:1px solid var(--line)"><td style="padding:3.4px 0;color:var(--blue-text)">Filtration Stages</td><td>3-Stage Advanced Filtration</td></tr>
      <tr style="border-bottom:1px solid var(--line)"><td style="padding:3.4px 0;color:var(--blue-text)">Flow Rate</td><td>Up to 15 GPM</td></tr>
      <tr style="border-bottom:1px solid var(--line)"><td style="padding:3.4px 0;color:var(--blue-text)">Operating Pressure</td><td>20 - 100 PSI</td></tr>
      <tr style="border-bottom:1px solid var(--line)"><td style="padding:3.4px 0;color:var(--blue-text)">Temperature Range</td><td>40°F - 100°F</td></tr>
      <tr style="border-bottom:1px solid var(--line)"><td style="padding:3.4px 0;color:var(--blue-text)">Connection Size</td><td>1" NPT</td></tr>
      <tr style="border-bottom:1px solid var(--line)"><td style="padding:3.4px 0;color:var(--blue-text)">Dimensions</td><td>24" x 10" x 54"</td></tr>
      <tr><td style="padding:3.4px 0;color:var(--blue-text)">Warranty</td><td>10 Years Limited Warranty</td></tr>
    </tbody>
  </table>
  <h3 class="abs" style="left:230px;top:420px;font-size:5.8px;font-weight:700;color:var(--blue-text)">WHAT'S INCLUDED</h3>
  <ul class="abs" style="left:230px;top:436px;list-style:none;font-size:4.4px;display:flex;flex-direction:column;gap:7.6px;line-height:1">
    <li>○ &nbsp;1 x Multi-Stage Filter System</li>
    <li>○ &nbsp;1 x Stainless Steel Housing</li>
    <li>○ &nbsp;3 x Pre-Filter Cartridges</li>
    <li>○ &nbsp;1 x Installation Kit</li>
    <li>○ &nbsp;1 x User Manual</li>
  </ul>

  <!-- CTA band -->
  <div class="abs" style="left:18px;top:528px;width:346px;height:38px;background:var(--blue);border-radius:4px;color:#fff">
    <div style="position:absolute;left:14px;top:8px;font-size:7.4px;font-weight:700">Ready to Transform Your Water?</div>
    <div style="position:absolute;left:14px;top:22px;font-size:4.6px">Contact us today for a free water test and personalized recommendation.</div>
    <span class="btn btn-white" style="position:absolute;right:34px;top:11px;width:106px;height:16px;color:var(--blue-dark)">SCHEDULE FREE CONSULTATION</span>
  </div>

  <h2 class="sec-title" style="top:579px;font-size:6.8px">COMPLETE YOUR SYSTEM</h2>
  <p class="sec-sub" style="top:591px;font-size:4.4px">Add these optional upgrades for maximum performance.</p>
  <div class="grid" style="left:18px;top:606px;gap:8px">
    <div class="pcard" style="width:74px;height:86px"><div class="img" role="img" aria-label="Pre-filter housing" style="margin-top:7px;width:30px;height:36px"></div><div class="name" style="margin-top:5px">Sediment Pre-Filter</div><p style="font-size:4px;color:var(--muted);line-height:1.4;margin-top:2px">Protect your system<br>from dirt and sand.</p><div class="more">Learn More →</div></div>
    <div class="pcard" style="width:74px;height:86px"><div class="img" role="img" aria-label="UV sterilizer" style="margin-top:7px;width:30px;height:36px"></div><div class="name" style="margin-top:5px">UV Sterilization</div><p style="font-size:4px;color:var(--muted);line-height:1.4;margin-top:2px">Eliminates bacteria<br>and viruses.</p><div class="more">Learn More →</div></div>
    <div class="pcard" style="width:74px;height:86px"><div class="img" role="img" aria-label="Water softener" style="margin-top:7px;width:30px;height:36px"></div><div class="name" style="margin-top:5px">Water Softener</div><p style="font-size:4px;color:var(--muted);line-height:1.4;margin-top:2px">Reduces hard water<br>and scale.</p><div class="more">Learn More →</div></div>
    <div class="pcard" style="width:74px;height:86px"><div class="img" role="img" aria-label="Ionization unit" style="margin-top:7px;width:30px;height:36px"></div><div class="name" style="margin-top:5px">Whole House<br>Ionization</div><p style="font-size:4px;color:var(--muted);line-height:1.4;margin-top:1px">Enhance water<br>alkalinity.</p><div class="more">Learn More →</div></div>
  </div>
  <div class="abs" style="left:18px;top:703px;width:346px;height:1px;background:var(--blue)"></div>
  <div class="abs" style="left:22px;top:711px;width:340px;display:flex;justify-content:space-between;font-size:4.2px;line-height:1.5">
    <div style="display:flex;gap:4px"><svg width="10" height="10" viewBox="0 0 24 24"><path d="M12 3c4 5 6 8 6 11a6 6 0 01-12 0c0-3 2-6 6-11z" fill="none" stroke="#1f4fb4" stroke-width="1.8"/></svg><div><b style="color:var(--blue-text)">Free Water Test</b><br><span style="color:var(--muted)">Professional analysis<br>of your water.</span></div></div>
    <div style="display:flex;gap:4px"><svg width="10" height="10" viewBox="0 0 24 24"><circle cx="12" cy="8" r="4" fill="none" stroke="#1f4fb4" stroke-width="1.8"/><path d="M4 21c1-5 15-5 16 0" fill="none" stroke="#1f4fb4" stroke-width="1.8"/></svg><div><b style="color:var(--blue-text)">Expert Installation</b><br><span style="color:var(--muted)">Certified technicians<br>you can trust.</span></div></div>
    <div style="display:flex;gap:4px"><svg width="10" height="10" viewBox="0 0 24 24"><path d="M12 2l8 3v6c0 5-3.5 9-8 11-4.5-2-8-6-8-11V5z" fill="none" stroke="#1f4fb4" stroke-width="1.8"/></svg><div><b style="color:var(--blue-text)">Lifetime Support</b><br><span style="color:var(--muted)">We're here whenever<br>you need us.</span></div></div>
    <div style="display:flex;gap:4px"><svg width="10" height="10" viewBox="0 0 24 24"><circle cx="12" cy="12" r="8" fill="none" stroke="#1f4fb4" stroke-width="1.8"/><path d="M8 12l3 3 5-6" fill="none" stroke="#1f4fb4" stroke-width="1.8"/></svg><div><b style="color:var(--blue-text)">Satisfaction</b><br><span style="color:var(--muted)">100% satisfaction<br>guaranteed.</span></div></div>
  </div>
</section>

<!-- ================= ABOUT US PAGE ================= -->
<section class="page about" style="left:409px;top:805px;width:383px;height:395px">
  <header class="site-header" style="height:40px">
    <div class="brand"><span class="brand-dot"></span><div class="brand-name">Mr. Clear Brook<br>Mr. Hot Kettle</div></div>
    <nav class="nav" style="gap:8px"><span class="on">HOME</span><span>PRODUCTS ⌄</span><span>ABOUT US</span><span>WHY CHOOSE US</span><span>RESOURCES ⌄</span><span>CONTACT US</span></nav>
    <div class="call" style="margin-left:8px"><svg width="8" height="8" viewBox="0 0 24 24"><path d="M6.6 10.8a15 15 0 006.6 6.6l2.2-2.2c.3-.3.7-.4 1-.2 1.1.4 2.3.6 3.6.6.6 0 1 .4 1 1V20c0 .6-.4 1-1 1A17 17 0 013 4c0-.6.4-1 1-1h3.5c.6 0 1 .4 1 1 0 1.3.2 2.5.6 3.6.1.3 0 .7-.2 1z" fill="#1f4fb4"/></svg><div>Call Us Now<br><b>(555) 014-2290</b></div></div>
  </header>
  <div class="ph" role="img" aria-label="Family sharing glasses of water in a bright kitchen" style="left:188px;top:43px;width:184px;height:128px;background:linear-gradient(135deg,#f1ede7,#d4c2ae 50%,#9bb3d2)"></div>
  <div class="abs" style="left:286px;top:146px;width:82px;height:28px;background:#fff;border-radius:4px;box-shadow:0 1px 4px rgba(0,0,0,.15);display:flex;align-items:center;gap:4px;padding:0 5px">
    <span class="ic" style="width:16px;height:16px;border:1px solid var(--blue)"><svg width="9" height="9" viewBox="0 0 24 24"><circle cx="12" cy="8" r="4" fill="none" stroke="#1f4fb4" stroke-width="2"/><path d="M4 21c1-5 15-5 16 0" fill="none" stroke="#1f4fb4" stroke-width="2"/></svg></span>
    <div style="line-height:1.2"><div style="font-size:7.4px;font-weight:600;color:var(--blue-text)">15+ Years</div><div style="font-size:4px;color:var(--blue-text)">of Trusted Service</div></div>
  </div>
  <p class="abs" style="left:14px;top:46px;font-size:4.6px;font-weight:700;color:var(--ink)">ABOUT US</p>
  <h1 class="abs" style="left:14px;top:54px;font-size:11.5px;font-weight:700;color:var(--blue-text);line-height:1.35">Your Partner in<br>Pure Water &amp;<br>Better Living</h1>
  <p class="abs" style="left:14px;top:104px;width:170px;font-size:4.5px;line-height:1.6;color:var(--muted)">At Mr. Clear Brook &amp; Mr. Hot Kettle, our mission is simple: to provide families with the highest quality water and air treatment solutions for a healthier, more comfortable life.</p>
  <p class="abs" style="left:14px;top:136px;width:170px;font-size:4.5px;line-height:1.6;color:var(--muted)">With years of experience and a commitment to excellence, we deliver innovative products, expert installation, and <b style="color:var(--ink)">unmatched customer support.</b></p>

  <h2 class="sec-title" style="top:183px;font-size:6.6px">OUR VALUES</h2>
  <div class="abs" style="left:14px;top:194px;width:355px;display:flex;justify-content:space-around;text-align:center;font-size:4.1px;color:var(--muted);line-height:1.5">
    <div style="width:60px"><svg width="16" height="16" viewBox="0 0 24 24"><circle cx="12" cy="12" r="8" fill="none" stroke="#1f4fb4" stroke-width="1.6"/><circle cx="12" cy="12" r="3" fill="none" stroke="#1f4fb4" stroke-width="1.6"/></svg><br><b style="color:var(--blue-text);font-size:4.6px">Quality</b><br>We use premium<br>components for<br>long-lasting<br>performance.</div>
    <div style="width:60px"><svg width="16" height="16" viewBox="0 0 24 24"><path d="M12 2l8 3v6c0 5-3.5 9-8 11-4.5-2-8-6-8-11V5z" fill="none" stroke="#1f4fb4" stroke-width="1.6"/><path d="M9 12l2 2 4-4" fill="none" stroke="#1f4fb4" stroke-width="1.6"/></svg><br><b style="color:var(--blue-text);font-size:4.6px">Integrity</b><br>Honest service<br>and transparent<br>recommendations<br>you can trust.</div>
    <div style="width:60px"><svg width="16" height="16" viewBox="0 0 24 24"><path d="M9 18h6M10 21h4M12 3a6 6 0 00-3 11v2h6v-2a6 6 0 00-3-11z" fill="none" stroke="#1f4fb4" stroke-width="1.6"/></svg><br><b style="color:var(--blue-text);font-size:4.6px">Innovation</b><br>Advanced technology<br>for the best water<br>and air treatment<br>solutions.</div>
    <div style="width:60px"><svg width="16" height="16" viewBox="0 0 24 24"><circle cx="12" cy="12" r="8" fill="none" stroke="#1f4fb4" stroke-width="1.6"/><path d="M12 16l-4-4a2 2 0 013-3l1 1 1-1a2 2 0 013 3z" fill="none" stroke="#1f4fb4" stroke-width="1.4"/></svg><br><b style="color:var(--blue-text);font-size:4.6px">Customer First</b><br>Your satisfaction<br>and health are<br>our top priority.</div>
  </div>

  <div class="abs" style="left:14px;top:268px;width:355px;height:38px;background:var(--blue-dark);border-radius:4px;display:flex;align-items:center;color:#fff;text-align:center">
    <div style="flex:1"><div style="font-size:11px;font-weight:600">10K+</div><div style="font-size:4.4px">Happy Customers</div></div>
    <div style="flex:1"><div style="font-size:11px;font-weight:600">15+</div><div style="font-size:4.4px">Years Experience</div></div>
    <div style="flex:1"><div style="font-size:11px;font-weight:600">100%</div><div style="font-size:4.4px">Satisfaction</div></div>
    <div style="flex:1"><div style="font-size:11px;font-weight:600">Top Rated</div><div style="font-size:4.4px">in Florida</div></div>
  </div>

  <h2 class="abs" style="left:14px;top:325px;font-size:6.6px;font-weight:700;color:var(--blue-text)">OUR COMMITMENT</h2>
  <p class="abs" style="left:14px;top:337px;width:150px;font-size:4.4px;line-height:1.6;color:var(--muted)">We stand behind our products and service with industry-leading warranties, professional installation, and lifetime support. When you choose us, you get more than just a product – you get peace of mind.</p>
  <div class="ph" role="img" aria-label="Branded service vans parked outside a suburban home" style="left:173px;top:320px;width:198px;height:75px;border-radius:0;background:linear-gradient(180deg,#d7e3f2,#eef1f5 45%,#b7c2d0)"></div>
</section>

</div>
</body>
</html>
```